Hadley & Partners, LLC Business Card 2016

We need a new business card design for a very important trade show coming up.

We are a compliance Consulting Firm. Our clients are stock brokerage firms and investment advisers.

I would like our logo on both sides of the card.

Info in the front of the card shold include:

Logo
First & Last Name
Title
Office #
Cell #
Email
Company Address (42 W. Calloway St., Suite 300 Pasadena, CA 91417

Back of the card should include the logo and url: www.hadleypartnersgroup.com

Target Market(s)

Stock Brokerage Firms and Investment Advisers

Industry/Entity Type

Financial Service

Contact Information for Business Card

Marcus J. Pellew
President
42 W. Calloway St., Suite 300
Pasadena, CA 91417
O 626.555.0147 ext. 204
C 818.555.0193
Email: marcus@hadleypartnersgroup.com
www.hadleypartnersgroup.com

Requirements
Nice to have
• The back of the card could be black with the logo with the white letters.
• I do want the front of the card to at least have the color logo with the black "Hadley & Partners Lettering.

```html
<!DOCTYPE html>
<html lang="en">
<head>
<meta charset="utf-8">
<title>Hadley &amp; Partners, LLC — Business Card</title>
<link rel="stylesheet" href="https://fonts.googleapis.com/css2?family=Open+Sans:wght@400;600;700&display=swap">
<style>
  :root {
    --page-bg: #2a2a2c;
    --card-white: #ffffff;
    --card-silver-light: #9a9fa6;
    --card-silver-dark: #4f545b;
    --brand-red: #c8252c;
    --ink-dark: #2b2b2b;
    --ink-body: #4a4a4a;
    --ink-muted: #7a7a7a;
    --url-light: #e9ebee;
  }
  * { box-sizing: border-box; margin: 0; padding: 0; }
  html, body {
    width: 1200px;
    height: 843px;
    overflow: hidden;
  }
  body {
    background: var(--page-bg);
    font-family: "Open Sans", Arial, sans-serif;
    display: flex;
    align-items: center;
    justify-content: center;
    gap: 36px;
  }
  .card {
    position: relative;
    width: 546px;
    height: 312px;
    border-radius: 3px;
    overflow: hidden;
  }
  .brand {
    display: flex;
    align-items: center;
    gap: 12px;
  }
  .brand-square {
    width: 30px;
    height: 30px;
    background: var(--brand-red);
  }
  .brand-name {
    font-weight: 600;
    font-size: 27px;
    letter-spacing: 0.5px;
    color: var(--ink-dark);
    white-space: nowrap;
  }

  /* Back side */
  .card-back {
    background: radial-gradient(ellipse at 50% 40%, var(--card-silver-light) 0%, var(--card-silver-dark) 85%);
    display: flex;
    flex-direction: column;
    align-items: center;
    justify-content: center;
  }
  .card-back .brand-name { color: var(--ink-dark); }
  .card-back .site-url {
    position: absolute;
    bottom: 40px;
    left: 0;
    right: 0;
    text-align: center;
    font-size: 12px;
    letter-spacing: 3px;
    color: var(--url-light);
  }

  /* Front side */
  .card-front {
    background: linear-gradient(160deg, var(--card-white) 55%, #eeeeee 100%);
  }
  .card-front .brand {
    position: absolute;
    top: 44px;
    right: 34px;
  }
  .card-front .brand-name { font-size: 24px; }
  .holder {
    position: absolute;
    left: 34px;
    top: 128px;
  }
  .holder-name {
    font-weight: 700;
    font-size: 20px;
    color: var(--brand-red);
    line-height: 1.2;
  }
  .holder-title {
    font-size: 13px;
    color: var(--ink-muted);
    line-height: 1.4;
  }
  .rule {
    position: absolute;
    left: 34px;
    right: 34px;
    top: 184px;
    height: 1px;
    background: var(--brand-red);
  }
  .contact {
    position: absolute;
    left: 34px;
    top: 196px;
    font-size: 12.5px;
    line-height: 1.7;
    color: var(--ink-body);
  }
  .contact .label {
    color: var(--brand-red);
    font-weight: 700;
  }
  .contact .gap { margin-left: 10px; }
</style>
</head>
<body>
  <section class="card card-back" aria-label="Card back">
    <div class="brand">
      <span class="brand-square"></span>
      <span class="brand-name">Hadley &amp; Partners</span>
    </div>
    <p class="site-url">www.hadleypartnersgroup.com</p>
  </section>

  <section class="card card-front" aria-label="Card front">
    <div class="brand">
      <span class="brand-square"></span>
      <span class="brand-name">Hadley &amp; Partners</span>
    </div>
    <div class="holder">
      <p class="holder-name">Marcus J. Pellew</p>
      <p class="holder-title">President</p>
    </div>
    <div class="rule"></div>
    <div class="contact">
      <p>42 W. Calloway St., Suite 300, Pasadena, CA 91417</p>
      <p><span class="label">P :</span> 626.555.0147 ext. 204 <span class="label gap">M :</span> 818.555.0193</p>
      <p>marcus@hadleypartnersgroup.com | www.hadleypartnersgroup.com</p>
    </div>
  </section>
</body>
</html>
```